Patient Report Folder for modern Chiropractic Clinic

We are looking for someone to design a patient folder and 3 simple info sheets to go along with it.

The design should be clean and masculine with an artsy touch. I am a fan of the Fra Mollego style drawings so would like the background to be a style of parchment paper. The info sheets should follow a similar style.

Please check the “Design Outline” pdf and the “Folder Design” file before getting started. The 3 info sheets are going to be placed in the pocket where “Attachment #3” will be.

- The format should be DIN A4 according to the printing details attached in the files section. Please see the ''Folder Design.jpg'' for the design of the folder.
- All the designs should be different and unique in nature but match each other.
- The text for Info Sheet #3 can be left blank.

It is probably best to take a look at the ''Design Outline'' file first to see how I envision the design to be. Please do not hesitate to ask me questions or to discuss ideas.

Target Market(s)

upper class audience with a focus on health and well-being

Industry/Entity Type

Chiropractic // Health

Requirements
Must have
• The colours should be fitting with the main colours in the logo: #1ccad5 and #b1b2b4
Nice to have
• Fra Mollego Style design and the background on parchment paper style. It is not a must but if anyone can come up with a suitable design and colorway that would be great.

```html
<!DOCTYPE html>
<html lang="en">
<head>
<meta charset="utf-8">
<title>Your Next Visit · Stress Builders</title>
<link href="https://fonts.googleapis.com/css2?family=Montserrat:wght@300;400;600&family=Nunito:wght@400&family=Allura&display=swap" rel="stylesheet">
<style>
  :root {
    --backdrop: #bdbcbe;
    --paper: #f2f2f0;
    --paper-shade: #e6e6e4;
    --teal: #1ccad5;
    --ink: #2b2b2b;
    --ink-soft: #555;
    --stone: #7b7b7b;
    --sage: #8fb0a8;
    --sage-band: #c4d6d1;
    --mist: #dde7e4;
    --ring: #9dbab3;
  }
  html, body {
    margin: 0; padding: 0;
    width: 1200px; height: 847px;
    overflow: hidden;
    background: var(--backdrop);
  }
  .spread {
    position: absolute;
    left: 63px; top: 43px;
    width: 1074px; height: 760px;
    display: flex;
  }
  .page {
    position: relative;
    width: 537px; height: 760px;
    background: var(--paper);
  }
  .page--left {
    background: linear-gradient(to right, var(--paper) 80%, var(--paper-shade));
    text-align: center;
    font-family: 'Nunito', sans-serif;
    color: var(--ink);
  }
  .page--right {
    background: linear-gradient(to right, var(--paper-shade), var(--paper) 15%);
  }
  .visit-title {
    margin: 0;
    padding-top: 70px;
    font-family: 'Montserrat', sans-serif;
    font-weight: 600;
    font-size: 20px;
    letter-spacing: 1.5px;
    color: var(--teal);
  }
  .visit-steps {
    list-style: none;
    margin: 70px 0 0; padding: 0;
  }
  .visit-step {
    font-size: 13.5px;
    line-height: 1.35;
    margin-bottom: 22px;
    letter-spacing: .3px;
  }
  .visit-step .dash { display: block; line-height: .6; }
  .smile {
    position: absolute;
    left: 0; right: 0; top: 650px;
    font-family: 'Montserrat', sans-serif;
    font-size: 26px;
    color: var(--teal);
  }
  .stress-art { position: absolute; inset: 0; }
  .stress-title {
    font-family: 'Montserrat', sans-serif;
    font-weight: 400;
    font-size: 62px;
    fill: var(--ink);
    letter-spacing: 2px;
  }
  .stress-script {
    font-family: 'Allura', cursive;
    font-size: 70px;
    fill: var(--ink);
  }
  .intro {
    font-family: 'Montserrat', sans-serif;
    font-size: 8.2px;
    fill: var(--ink-soft);
  }
  .circle-head {
    font-family: 'Montserrat', sans-serif;
    font-size: 15px;
    letter-spacing: 1px;
    fill: var(--ink);
  }
  .circle-body {
    font-family: 'Montserrat', sans-serif;
    font-size: 8.5px;
    fill: var(--ink);
  }
</style>
</head>
<body>
<main class="spread">
  <section class="page page--left">
    <h2 class="visit-title">YOUR NEXT VISIT</h2>
    <ul class="visit-steps">
      <li class="visit-step">Make yourself at home<span class="dash">—</span>Take of your shoes and jacket</li>
      <li class="visit-step">Let us know you’re here<span class="dash">—</span>Check in at the front desk</li>
      <li class="visit-step">Get comfy<span class="dash">—</span>Take a seat in the waiting area or the designated adjusting room</li>
      <li class="visit-step">Be excited and be ready<span class="dash">—</span>Take of your belt, empty your pockets and take a seat on “The Chair”</li>
      <li class="visit-step">ADJUSTING TIME</li>
      <li class="visit-step">Time to say goodbye<span class="dash">—</span>Our front desk will help you with EVERYTHING else you need</li>
      <li class="visit-step">Be a better version of yourself<span class="dash">—</span>Take a 10 minute walk</li>
    </ul>
    <div class="smile">:)</div>
  </section>

  <section class="page page--right">
    <svg class="stress-art" viewBox="0 0 537 760" width="537" height="760">
      <rect class="title-band" x="125" y="58" width="200" height="40" fill="var(--sage-band)"/>
      <text class="stress-title" x="245" y="92" text-anchor="middle">STRESS</text>
      <text class="stress-script" x="270" y="158" text-anchor="middle">builders</text>

      <text class="intro" text-anchor="middle">
        <tspan x="268" y="198">Try your best to remove or reduce these stressors from your life as possible. By reducing stress on</tspan>
        <tspan x="268" y="209">your body, you increase your parasympathetic nervous system’s influence, which will enable your</tspan>
        <tspan x="268" y="220">body’s innate healing to flourish. This in turn will boost your healing and you will reduce injury</tspan>
        <tspan x="268" y="231">and sickness.</tspan>
      </text>

      <circle cx="290" cy="370" r="100" fill="var(--stone)" opacity=".9"/>
      <circle cx="296" cy="364" r="104" fill="none" stroke="var(--ring)" stroke-width="2"/>
      <circle cx="200" cy="570" r="100" fill="var(--sage)" opacity=".9"/>
      <circle cx="194" cy="562" r="104" fill="none" stroke="var(--ring)" stroke-width="2"/>
      <circle cx="385" cy="535" r="100" fill="var(--mist)" opacity=".85"/>
      <circle cx="380" cy="530" r="104" fill="none" stroke="var(--ring)" stroke-width="2"/>

      <text class="circle-head" x="290" y="325" text-anchor="middle">EMOTIONAL</text>
      <text class="circle-body" text-anchor="middle">
        <tspan x="290" y="360">your body being in a constant state of</tspan>
        <tspan x="290" y="372">fight or flight, rather than</tspan>
        <tspan x="290" y="384">in a relaxed, parasympathetic state</tspan>
      </text>

      <text class="circle-head" x="190" y="545" text-anchor="middle">CHEMICAL</text>
      <text class="circle-body" text-anchor="middle">
        <tspan x="190" y="575">toxins in food, drink, pharmaceuticals,</tspan>
        <tspan x="190" y="587">skincare and any cleaning products</tspan>
        <tspan x="190" y="599">all put stress on the body</tspan>
      </text>

      <text class="circle-head" x="395" y="520" text-anchor="middle">PHYSICAL</text>
      <text class="circle-body" text-anchor="middle">
        <tspan x="395" y="548">any physical influence your body has</tspan>
        <tspan x="395" y="560">had to compensate for, such as,</tspan>
        <tspan x="395" y="572">sports injuries or car accidents</tspan>
      </text>

      <rect role="img" aria-label="Fine line drawing of an open hand holding flower stems" x="190" y="150" width="210" height="420" rx="60" fill="#8a8a8a" opacity=".12"/>
      <rect role="img" aria-label="Small line drawing of a leafy sprig" x="440" y="640" width="85" height="100" rx="20" fill="#9a9a9a" opacity=".18"/>
    </svg>
  </section>
</main>
</body>
</html>
```